Tova Brisk Fitness Coaching Project

I am a personal trainer based in London. My services include one-on-one PT sessions, bootcamps.
I would like the design to be minimalistic. With light colours: white, pink, purple.
I specialise in weight loss, flexibility, mobility.

Tova Penrick
Personal Trainer
Email: tova.penrick@mailgrove.net
tel: 07500 918 243
Instagram: Tova Brisk

Target Market(s)

adults, mostly females (age 18-50).

Industry/Entity Type

Fitness

Contact Information for Business Card

Tova Penrick
Personal Trainer
tel: 07500 918 243
Instagram: Tova Brisk

Font styles to use
Serif

Colors
eea4c8
fbd4d5
fdf9cf
cfeae6
cee9f5

Requirements
Nice to have
• minimalistic style
• easy to read and remember

```html
<!DOCTYPE html>
<html lang="en">
<head>
<meta charset="utf-8">
<title>Tova Brisk Fitness Coaching – Business Card</title>
<link rel="stylesheet" href="https://fonts.googleapis.com/css2?family=Bodoni+Moda:wght@600;700&family=Montserrat:wght@400;500&family=Tinos&display=swap">
<style>
  :root {
    --backdrop: #2a2a2a;
    --card-white: #f7f7f7;
    --card-dark: #14181a;
    --card-dark-glow: #1f2b22;
    --ink-grey: #5a5a5a;
    --accent-pink: #eea4c8;
    --text-light: #ffffff;
    --text-dark: #1e1e1e;
    --photo-warm: #b9754a;
    --photo-deep: #3a2418;
    --photo-light: #e9c9a8;
  }
  * { margin: 0; padding: 0; box-sizing: border-box; }
  html, body {
    width: 1200px;
    height: 997px;
    overflow: hidden;
    background: var(--backdrop);
  }
  .canvas {
    position: relative;
    width: 1200px;
    height: 997px;
    display: flex;
    flex-direction: column;
    align-items: center;
    justify-content: center;
    gap: 48px;
  }
  .card {
    position: relative;
    width: 700px;
    height: 400px;
    border-radius: 22px;
    overflow: hidden;
    box-shadow: 0 18px 40px rgba(0, 0, 0, 0.45);
  }

  /* Back side: contact details */
  .card-back { background: var(--card-white); }
  .contact-list {
    position: absolute;
    left: 58px;
    bottom: 62px;
    list-style: none;
    font-family: "Tinos", serif;
    font-size: 25px;
    color: var(--ink-grey);
  }
  .contact-row {
    display: flex;
    align-items: center;
    gap: 28px;
    margin-top: 14px;
  }
  .contact-item {
    display: flex;
    align-items: center;
    gap: 8px;
    white-space: nowrap;
  }
  .contact-icon { width: 20px; height: 20px; flex: none; }
  .social-dot {
    width: 18px;
    height: 18px;
    border-radius: 50%;
    background: var(--accent-pink);
    flex: none;
  }

  /* Front side: name and photo */
  .card-front {
    background: radial-gradient(circle at 30% 40%, var(--card-dark-glow), var(--card-dark) 65%);
  }
  .portrait {
    position: absolute;
    right: 0;
    top: 0;
    width: 52%;
    height: 100%;
    background: radial-gradient(ellipse at 45% 40%, var(--photo-light) 0%, var(--photo-warm) 40%, var(--photo-deep) 85%);
  }
  .identity {
    position: absolute;
    left: 0;
    top: 188px;
    width: 330px;
    display: flex;
    flex-direction: column;
    align-items: flex-end;
  }
  .name {
    padding-right: 4px;
    font-family: "Bodoni Moda", serif;
    font-weight: 700;
    font-size: 33px;
    letter-spacing: 1px;
    color: var(--text-light);
    line-height: 1;
    white-space: nowrap;
  }
  .role {
    margin-top: 8px;
    padding-right: 4px;
    font-family: "Montserrat", sans-serif;
    font-weight: 400;
    font-size: 14px;
    letter-spacing: 5px;
    color: var(--text-light);
    white-space: nowrap;
  }
  .specialties {
    margin-top: 10px;
    padding: 4px 10px 3px;
    border-radius: 5px 5px 0 0;
    background: var(--text-light);
    font-family: "Montserrat", sans-serif;
    font-weight: 500;
    font-size: 12px;
    line-height: 1.2;
    color: var(--text-dark);
    white-space: nowrap;
  }
  .accent-band {
    width: 100%;
    height: 18px;
    background: var(--text-light);
    border-radius: 0 5px 5px 0;
  }
</style>
</head>
<body>
  <main class="canvas">
    <section class="card card-back" aria-label="Business card back">
      <ul class="contact-list">
        <li class="contact-row">
          <span class="contact-item">
            <svg class="contact-icon" viewBox="0 0 20 20" aria-hidden="true">
              <rect x="1" y="4" width="18" height="13" rx="2" fill="var(--accent-pink)"/>
              <path d="M5 4 Q10 0 15 4" fill="none" stroke="var(--accent-pink)" stroke-width="2"/>
              <circle cx="10" cy="11" r="3" fill="var(--card-white)"/>
            </svg>
            07500 918 243
          </span>
          <span class="contact-item">
            <svg class="contact-icon" viewBox="0 0 20 20" aria-hidden="true">
              <rect x="1" y="4" width="18" height="12" rx="1.5" fill="var(--accent-pink)"/>
              <path d="M2 5 L10 11 L18 5" fill="none" stroke="var(--card-white)" stroke-width="1.5"/>
            </svg>
            tova.penrick@mailgrove.net
          </span>
        </li>
        <li class="contact-row">
          <span class="contact-item">
            <span class="social-dot" aria-hidden="true"></span>
            picfeed.net/Tova_Brisk
          </span>
        </li>
      </ul>
    </section>

    <section class="card card-front" aria-label="Business card front">
      <div class="portrait" role="img" aria-label="Portrait photo of the trainer outdoors in warm sunlight"></div>
      <div class="identity">
        <h1 class="name">TOVA PENRICK</h1>
        <p class="role">Personal Trainer</p>
        <p class="specialties">Weight Loss • Flexibility • Mobility</p>
        <div class="accent-band"></div>
      </div>
    </section>
  </main>
</body>
</html>
```